Stellwick Instruments Pacific - Business Cards

I would like a design developed using the logo (number 27386059) previously developed and attached. The information needs to include everything shown on the attached email title block, arranged to suit a business format. I would like a white background, with no other graphics added.
I need an editable version (e.g. MSWord) so I can change the name shown on the business card for others.

Target Market(s)

Mining & Heavy Manufacturing industries

Industry/Entity Type

Mining

Contact Information for Business Card

Refer to attached email title block in MSWord format for the details to be included.

Colors

Designer to choose colors to be used in the design.

Requirements
Must have
• White background, and fonts and text colour to match the unique font in the logo.
Nice to have
• the website address to be shown along the bottom of the card, as it is quite long.
Should not have
• Dark background, or unnecessary graphics

```html
<!DOCTYPE html>
<html lang="en">
<head>
<meta charset="utf-8">
<title>Stellwick Instruments Pacific – Business Card</title>
<link href="https://fonts.googleapis.com/css2?family=Roboto:wght@300;400;700&display=swap" rel="stylesheet">
<style>
  :root {
    --page-bg: #e9e9ea;
    --card-bg: #ffffff;
    --brand-blue: #1f9ad6;
    --brand-blue-dark: #1580b8;
    --ink: #2a2d31;
    --ink-soft: #6b6f75;
    --rule-white: rgba(255,255,255,0.85);
  }
  * { box-sizing: border-box; margin: 0; padding: 0; }
  html, body {
    width: 1200px; height: 1023px; overflow: hidden;
    background: var(--page-bg);
    font-family: "Roboto", Arial, sans-serif;
  }
  .stage {
    width: 1200px; height: 1023px;
    display: flex; align-items: center; justify-content: center;
  }
  .business-card {
    position: relative;
    width: 900px; height: 514px;
    background: var(--card-bg);
    box-shadow: 0 10px 30px rgba(0,0,0,0.12);
    overflow: hidden;
  }
  .brand {
    position: absolute; left: 60px; top: 58px;
    display: flex; align-items: center; gap: 22px;
  }
  .brand-mark {
    width: 74px; height: 74px; border-radius: 50%;
    background: var(--brand-blue);
  }
  .brand-name {
    font-weight: 400; font-size: 34px; line-height: 1.1;
    letter-spacing: 2px; text-transform: uppercase;
    color: var(--ink);
  }
  .name-band {
    position: absolute; left: 0; right: 0; top: 178px; height: 70px;
    background: var(--brand-blue);
  }
  .name-band::before, .name-band::after {
    content: ""; position: absolute; left: 0; right: 0; height: 2px;
    background: var(--rule-white);
  }
  .name-band::before { top: 8px; }
  .name-band::after { bottom: 8px; }
  .person-name {
    position: absolute; left: 0; right: 0; top: 50%; transform: translateY(-50%);
    text-align: center; color: #fff;
    font-weight: 700; font-size: 30px;
  }
  .person-role {
    position: absolute; left: 0; right: 0; top: 256px;
    text-align: center; color: var(--ink-soft);
    font-weight: 400; font-size: 20px;
  }
  .contact-list {
    position: absolute; left: 0; right: 0; top: 298px;
    list-style: none; text-align: center;
    color: var(--ink-soft); font-weight: 300; font-size: 20px; line-height: 30px;
  }
  .website {
    position: absolute; left: 0; right: 0; bottom: 62px;
    text-align: center; color: var(--ink-soft);
    font-weight: 300; font-size: 20px;
  }
  .abn-tag {
    position: absolute; right: 60px; bottom: 18px;
    background: var(--brand-blue); color: #fff;
    font-weight: 400; font-size: 16px;
    padding: 5px 12px;
  }
</style>
</head>
<body>
<main class="stage">
  <section class="business-card">
    <header class="brand">
      <span class="brand-mark" aria-hidden="true"></span>
      <span class="brand-name">Stellwick<br>Instruments<br>Pacific</span>
    </header>

    <div class="name-band">
      <h1 class="person-name">Renato (Ren) Valli</h1>
    </div>
    <p class="person-role">Director</p>

    <ul class="contact-list">
      <li>Email: renato.valli@stellwickpacific.com.au</li>
      <li>Phone: +61 432 718 905</li>
      <li>Skype: swi.renato.valli</li>
      <li>PO BOX 46, Carrington NSW 2294, AUSTRALIA</li>
    </ul>

    <p class="website">www.stellwickpacific.com.au</p>
    <p class="abn-tag">ABN 48 302 715 964</p>
  </section>
</main>
</body>
</html>
```